Rental Equipment Flyer

Summit Heater Leasing. 833-584-1967. www.summitheaterleasing.example
Flyer for Rental boilers, Rental DA tank, Rental water softeners.

Please include a partnered with section: Harbor Steam & Thermal, LLC space and include Harbors logo with 866-419-5382. Logo Attached.

```html
<!DOCTYPE html>
<html lang="en">
<head>
<meta charset="utf-8">
<title>Summit Heater Leasing – Rental Equipment Flyer</title>
<link href="https://fonts.googleapis.com/css2?family=Poppins:ital,wght@0,400;0,500;0,600;0,700;0,800;1,600&display=swap" rel="stylesheet">
<style>
  :root {
    --orange: #fa5a0a;
    --blue: #2196d3;
    --navy: #1d4fa3;
    --ink: #1a1a1a;
    --body: #333333;
    --gold: #d4b06a;
    --white: #ffffff;
    --bg: #6b6b6b;
  }
  * { margin: 0; padding: 0; box-sizing: border-box; }
  html, body { width: 1200px; height: 1001px; overflow: hidden; background: var(--bg); }
  body { font-family: "Poppins", sans-serif; position: relative; }
  .flyer {
    position: absolute; left: 260px; top: 19px;
    width: 739px; height: 1047px;
    background: var(--white);
    transform: scale(0.92); transform-origin: top left;
    overflow: hidden;
    box-shadow: 0 10px 30px rgba(0,0,0,.35);
  }
  .flyer__shapes { position: absolute; inset: 0; }
  .brand {
    position: absolute; left: 90px; top: 105px;
    display: flex; align-items: center; gap: 12px;
    color: var(--navy); font-weight: 700; font-size: 26px;
  }
  .brand__mark { width: 20px; height: 20px; background: var(--orange); }
  .hero { position: absolute; left: 72px; top: 300px; color: var(--white); }
  .hero__title { font-size: 50px; font-weight: 700; line-height: 1.02; text-shadow: 0 2px 4px rgba(0,0,0,.4); }
  .hero__sub { font-size: 23px; font-weight: 500; margin-top: 8px; text-shadow: 0 1px 3px rgba(0,0,0,.5); }
  .col-heading { font-size: 23px; font-weight: 600; color: var(--ink); margin-bottom: 10px; }
  .solutions { position: absolute; left: 72px; top: 583px; width: 300px; }
  .solution { margin-bottom: 8px; }
  .solution__name { display: flex; align-items: center; gap: 8px; font-size: 22px; font-weight: 600; color: var(--orange); line-height: 1.3; }
  .solution__desc { font-size: 15.5px; color: var(--body); padding-left: 28px; line-height: 1.45; }
  .tick { width: 18px; height: 18px; flex: none; }
  .divider { position: absolute; left: 377px; top: 560px; width: 2px; height: 290px; background: var(--orange); }
  .reasons { position: absolute; left: 400px; top: 583px; width: 320px; }
  .reason { display: flex; align-items: center; gap: 7px; font-size: 15.5px; color: var(--ink); line-height: 1.8; }
  .partner__label { font-size: 12.5px; font-style: italic; font-weight: 600; color: var(--ink); margin-top: 12px; }
  .partner__name { display: flex; align-items: center; gap: 8px; font-size: 19px; font-weight: 500; color: var(--ink); margin-top: 10px; padding-bottom: 8px; border-bottom: 1px solid var(--gold); width: 250px; }
  .partner__dot { width: 14px; height: 14px; border-radius: 50%; background: var(--gold); flex: none; }
  .partner__phone { display: flex; align-items: center; gap: 8px; font-size: 28px; font-weight: 700; color: var(--gold); margin-top: 6px; letter-spacing: 1px; }
  .cta {
    position: absolute; left: 42px; top: 873px; width: 648px; height: 56px;
    background: var(--orange); border-radius: 28px;
    display: flex; align-items: center; justify-content: center; gap: 14px;
    color: var(--white);
  }
  .cta__label { font-size: 20px; font-weight: 600; }
  .cta__phone { font-size: 34px; font-weight: 800; letter-spacing: 1px; }
  .website { position: absolute; left: 0; right: 0; top: 940px; text-align: center; font-size: 21px; font-weight: 700; letter-spacing: 2px; color: var(--ink); }
</style>
</head>
<body>
<article class="flyer">
  <svg class="flyer__shapes" viewBox="0 0 739 1047" width="739" height="739" style="height:1047px">
    <defs>
      <linearGradient id="photoTone" x1="0" y1="0" x2="1" y2="1">
        <stop offset="0" stop-color="#9a9590"/>
        <stop offset=".45" stop-color="#4a4642"/>
        <stop offset="1" stop-color="#2c2a28"/>
      </linearGradient>
    </defs>
    <g role="img" aria-label="Photo of an industrial boiler room with rental boilers and burners">
      <polygon points="0,300 739,128 739,430 0,545" fill="url(#photoTone)"/>
    </g>
    <polygon points="80,265 739,100 739,130 0,302 0,285" fill="var(--orange)"/>
    <polygon points="370,497 739,430 739,470 665,556" fill="var(--blue)"/>
    <polygon points="0,545 739,420 739,432 370,497 0,570" fill="var(--orange)"/>
  </svg>

  <div class="brand"><span class="brand__mark"></span>Summit Heater Leasing</div>

  <header class="hero">
    <h1 class="hero__title">Power When<br>You Need It</h1>
    <p class="hero__sub">Fast, Reliable, Ready to Go!</p>
  </header>

  <section class="solutions">
    <h2 class="col-heading">Our rental Solutions</h2>
    <div class="solution">
      <div class="solution__name"><svg class="tick" viewBox="0 0 20 20"><path d="M3 11l5 5L17 4" fill="none" stroke="var(--orange)" stroke-width="2.5"/></svg>Rental Boilers</div>
      <p class="solution__desc">Dependable, high-performance units</p>
    </div>
    <div class="solution">
      <div class="solution__name"><svg class="tick" viewBox="0 0 20 20"><path d="M3 11l5 5L17 4" fill="none" stroke="var(--orange)" stroke-width="2.5"/></svg>Rental DA Tanks</div>
      <p class="solution__desc">Efficient and easy to integrate</p>
    </div>
    <div class="solution">
      <div class="solution__name"><svg class="tick" viewBox="0 0 20 20"><path d="M3 11l5 5L17 4" fill="none" stroke="var(--orange)" stroke-width="2.5"/></svg>Rental Water Softeners</div>
      <p class="solution__desc">Protect your system and extend equipment life</p>
    </div>
  </section>

  <div class="divider"></div>

  <section class="reasons">
    <h2 class="col-heading">Why Choose Us?</h2>
    <div class="reason"><svg class="tick" viewBox="0 0 20 20"><path d="M3 11l5 5L17 4" fill="none" stroke="var(--orange)" stroke-width="2.5"/></svg>24/7 Emergency Support</div>
    <div class="reason"><svg class="tick" viewBox="0 0 20 20"><path d="M3 11l5 5L17 4" fill="none" stroke="var(--orange)" stroke-width="2.5"/></svg>Rapid Delivery &amp; Setup</div>
    <div class="reason"><svg class="tick" viewBox="0 0 20 20"><path d="M3 11l5 5L17 4" fill="none" stroke="var(--orange)" stroke-width="2.5"/></svg>Trusted by Industry Leaders</div>
    <p class="partner__label">In Partnership With</p>
    <div class="partner__name"><span class="partner__dot"></span>Harbor Steam &amp; Thermal</div>
    <div class="partner__phone">
      <svg width="18" height="18" viewBox="0 0 24 24"><path d="M6.6 10.8a15 15 0 006.6 6.6l2.2-2.2a1 1 0 011-.25 11.4 11.4 0 003.6.57 1 1 0 011 1V20a1 1 0 01-1 1A17 17 0 013 4a1 1 0 011-1h3.5a1 1 0 011 1c0 1.25.2 2.45.57 3.57a1 1 0 01-.25 1z" fill="var(--ink)"/></svg>
      866-419-5382
    </div>
  </section>

  <div class="cta">
    <span class="cta__label">CALL US TODAY:</span>
    <svg width="24" height="24" viewBox="0 0 24 24"><path d="M6.6 10.8a15 15 0 006.6 6.6l2.2-2.2a1 1 0 011-.25 11.4 11.4 0 003.6.57 1 1 0 011 1V20a1 1 0 01-1 1A17 17 0 013 4a1 1 0 011-1h3.5a1 1 0 011 1c0 1.25.2 2.45.57 3.57a1 1 0 01-.25 1z" fill="var(--white)"/></svg>
    <span class="cta__phone">833-584-1967</span>
  </div>

  <p class="website">WWW.SUMMITHEATERLEASING.EXAMPLE</p>
</article>
</body>
</html>
```